Visitenkarten
Zielgruppe
Zeitarbeit Personalvermittlung Arbeitsvermittlung Arbeitnehmerüberlassung
Zielgruppe:
Akademiker
Fachkräfte
Politiker
Ingenieur
wichtige Akteure der Gesellschaft
Kommunen
Vereinigungen
Aufgabenstellung
Wir benötigen schlichte und dezente, aber eindrucksvolle,exklusive Visitenkarten mit unserem Logo.
Aufbau:
Vorname, Name
Position
Telefon
Mobil
E-Mail
Fax
Unsere Website: http://www.veltranos-stellen.de
Wir sind 2 Geschäftsführer also bitte für beide Namen
Dies benötigen wir als PSD, PDF, JPG, sodass wir selbst die Angaben nach Belieben eintragen können.

```html
<!DOCTYPE html>
<html lang="de">
<head>
<meta charset="utf-8">
<title>Veltranos Visitenkarten</title>
<link href="https://fonts.googleapis.com/css2?family=Source+Sans+3:ital,wght@0,300;0,400;1,300&display=swap" rel="stylesheet">
<style>
  :root {
    --ink: #333333;
    --ink-soft: #555555;
    --orange: #ec6a0a;
    --orange-light: #f39200;
    --paper: #ffffff;
    --ring-grey: #6f6f6f;
    --ring-orange: #f0914f;
  }
  * { margin: 0; padding: 0; box-sizing: border-box; }
  html, body { width: 848px; height: 1200px; overflow: hidden; background: var(--paper); }
  body { position: relative; font-family: "Source Sans 3", Arial, sans-serif; color: var(--ink); }

  .card {
    position: absolute;
    left: 186px;
    width: 482px;
    height: 312px;
    background: var(--paper);
    border: 1px solid #e4e4e4;
    box-shadow: 2px 5px 7px rgba(0,0,0,0.28);
    overflow: hidden;
  }
  .card--front { top: 31px; }
  .card--front-web { top: 388px; }
  .card--back { top: 817px; }

  .brand { position: absolute; left: 0; right: 0; text-align: center; }
  .brand__dot {
    display: block; margin: 0 auto 6px;
    width: 62px; height: 62px; border-radius: 50%;
    background: var(--orange);
  }
  .brand__name {
    display: block;
    font-weight: 300; font-size: 88px; line-height: 78px;
    letter-spacing: -1px; color: var(--ink);
  }
  .brand__tagline {
    display: block; margin-top: 12px;
    font-weight: 400; font-size: 13px; letter-spacing: 6.2px;
    color: var(--ink); padding-left: 6px;
  }
  .card--front .brand { top: 72px; }
  .card--front-web .brand { top: 56px; }

  .web-band {
    position: absolute; left: 0; right: 0; bottom: 0; height: 40px;
    background: linear-gradient(90deg, var(--orange), var(--orange-light));
    color: var(--paper); font-size: 19px; text-align: center; line-height: 40px;
  }

  .brand-small { position: absolute; left: 36px; top: 18px; display: flex; align-items: flex-start; gap: 14px; }
  .brand-small__dot { width: 42px; height: 42px; border-radius: 50%; background: var(--orange); margin-top: 4px; }
  .brand-small__name { font-weight: 300; font-size: 44px; line-height: 40px; color: var(--ink); letter-spacing: -0.5px; display: block; }
  .brand-small__tagline { display: block; margin-top: 4px; font-size: 8px; letter-spacing: 2.6px; color: var(--ink); }

  .contact { position: absolute; left: 113px; top: 110px; font-weight: 300; color: var(--ink-soft); }
  .contact__name { font-weight: 400; font-size: 20px; color: var(--ink); line-height: 24px; }
  .contact__role { font-style: italic; font-size: 15px; line-height: 20px; }
  .contact__lines { margin-top: 24px; display: grid; grid-template-columns: 71px auto; font-size: 15px; line-height: 22px; }
  .contact__mail { margin-top: 16px; font-size: 15px; }
  .accent-band {
    position: absolute; left: 0; right: 0; bottom: 0; height: 12px;
    background: linear-gradient(90deg, var(--orange), var(--orange-light));
  }

  .decor {
    position: absolute; left: 0; top: 1040px; width: 240px; height: 160px;
    background: linear-gradient(90deg, rgba(111,111,111,0.25), rgba(240,145,79,0.3));
    border-top-right-radius: 120px;
  }
</style>
</head>
<body>
  <div class="decor" role="img" aria-label="Dekoratives Ringmotiv in Grau und Orange"></div>

  <section class="card card--front">
    <div class="brand">
      <span class="brand__dot"></span>
      <span class="brand__name">veltranos</span>
      <span class="brand__tagline">PERSONALDIENSTLEISTUNGEN</span>
    </div>
  </section>

  <section class="card card--front-web">
    <div class="brand">
      <span class="brand__dot"></span>
      <span class="brand__name">veltranos</span>
      <span class="brand__tagline">PERSONALDIENSTLEISTUNGEN</span>
    </div>
    <div class="web-band">www.veltranos-stellen.de</div>
  </section>

  <section class="card card--back">
    <div class="brand-small">
      <span class="brand-small__dot"></span>
      <div>
        <span class="brand-small__name">veltranos</span>
        <span class="brand-small__tagline">PERSONALDIENSTLEISTUNGEN GMBH</span>
      </div>
    </div>
    <div class="contact">
      <div class="contact__name">Konrad Albers</div>
      <div class="contact__role">Geschäftsführung</div>
      <div class="contact__lines">
        <span>Telefon:</span><span>+49 (0) 621&nbsp;&nbsp;&nbsp;48 72 10</span>
        <span>Telefax:</span><span>+49 (0) 621&nbsp;&nbsp;&nbsp;48 72 19</span>
        <span>Mobil:</span><span>+49 (0) 151&nbsp;&nbsp;&nbsp;70 38 415</span>
      </div>
      <div class="contact__mail">k.albers@veltranos-stellen.de</div>
    </div>
    <div class="accent-band"></div>
  </section>
</body>
</html>
```